Flyer Vacation Gift Certificate

I need to create a beautiful flyer 8.5 x 11 PDF format flyer design. <br/><br/>Instructions:<br/>The flyer will really be a gift voucher for a las vegas vacation getaway. So must have a Las Vegas Theme exciting fun<br/><br/>The voucher should have two modules that will be editable. <br/>Must have a "Compliments Of" area and also must have an "Exclusively For" area<br/><br/>Keep in mind that this flyer will be printed so keep that in mind :)<br/><br/>Here the is the content for the vacation voucher:<br/><br/>There is no doubt that Las Vegas is one of the hottest travel destinations around the world. In fact, some people would even go as far as<br/>saying that perhaps it is THE hottest place to visit. Enjoy up to 4 nights of resort/casino accommodations in exciting Las Vegas, NV. Millions of people travel to this exciting city each year to enjoy its thrills. Thanks to the business you received this certificate from, now you can enjoy exciting Las Vegas, NV too!<br/><br/>Features:<br/>*Travel 7 Days A Week<br/>*Stay Your Choice Of Nights (1-4 Nights)<br/>*Good For Two Adults & Two Children<br/>*Pay Just The Taxes & Fees<br/>*Multiple Travel Date Requests Allowed<br/>*Fully Transferable To Another Person<br/>*Just A 30 Days Advance Notice Required<br/>*You Will Have 12 Months To Complete Travel After Redemption<br/><br/>HOW CAN WE DO THIS?<br/><br/>We contract with the world leading hotel chains and resorts to help them fill their otherwise empty rooms.<br/><br/>We help fill empty rooms which the hotels, resorts and cruise lines turn into additional revenue from other areas of their property and future bookings.<br/><br/>Hotels rarely experience full occupancy, yet they remain open, providing rooms and services at fixed costs. So when hotels give out their rooms by partnering with marketing companies like us, they might miss out on the room fee, but they already didn't have that in the first place, at least now they have the opportunity to gain a customer for their in-house restaurants, room service, their casinos, an extra day stay, future bookings, etc.<br/><br/>VIEW ALL THE DETAILS OF THIS SPECIAL OFFER AND REDEEM ONLINE AT <br/>WWW.TOPAZVOUCHERDESK.COM<br/><br/>Certificate ID # 47261-38504<br/>Expires 02/29/2020<br/><br/><br/>*terms and conditions apply see website for details<br/><br/>KEEP IN MIND THE EXAMPLES I AM UPLOADING ARE SIMPLY TO SHOW YOU THAT THEY CONTAIN THE "COMPLIMENTS OF" AND "EXCLUSIVELY FOR" ELEMENTS. THESE MUST BE INCLUDED IN NEW DESIGN. PLEASE ONLY USE THE CONTENT I PROVIDED IN BRIEF, DONT USE CONTENT FROM EXAMPLES.

Target Market(s)

CONSUMERS THAT HAVE BEEN REWARDED WITH A VACATION CERTIFICATE FOR DOING BUSINESS WITH A COMPANY.

COMPANIES USE THESE AS MARKETING INCENTIVES TO ATTRACT MORE CUSTOMERS AND TO REWARD LOYALTY, ETC.

Industry/Entity Type

Travel Industry

Colors

Designer to choose colors to be used in the design.

Requirements
Must have
• I need to create a beautiful flyer 8.5 x 11 PDF format flyer design.
• Instructions:
• The flyer will really be a gift voucher for a las vegas vacation getaway. So must have a Las Vegas Theme exciting fun
• The voucher should have two modules that will be editable.
• Must have a "Compliments Of" area and also must have an "Exclusively For" area
• Keep in mind that this flyer will be printed so keep that in mind :)
• Here the is the content for the vacation voucher:
• There is no doubt that Las Vegas is one of the hottest travel destinations around the world. In fact, some people would even go as far as
• saying that perhaps it is THE hottest place to visit. Enjoy up to 4 nights of resort/casino accommodations in exciting Las Vegas, NV. Millions of people travel to this exciting city each year to enjoy its thrills. Thanks to the business you received this certificate from, now you can enjoy exciting Las Vegas, NV too!
• Features:
• *Travel 7 Days A Week
• *Stay Your Choice Of Nights (1-4 Nights)
• *Good For Two Adults & Two Children
• *Pay Just The Taxes & Fees
• *Multiple Travel Date Requests Allowed
• *Fully Transferable To Another Person
• *Just A 30 Days Advance Notice Required
• *You Will Have 12 Months To Complete Travel After Redemption
• HOW CAN WE DO THIS?
• We contract with the world leading hotel chains and resorts to help them fill their otherwise empty rooms.
• We help fill empty rooms which the hotels, resorts and cruise lines turn into additional revenue from other areas of their property and future bookings.
• Hotels rarely experience full occupancy, yet they remain open, providing rooms and services at fixed costs. So when hotels give out their rooms by partnering with marketing companies like us, they might miss out on the room fee, but they already didn't have that in the first place, at least now they have the opportunity to gain a customer for their in-house restaurants, room service, their casinos, an extra day stay, future bookings, etc.
• VIEW ALL THE DETAILS OF THIS SPECIAL OFFER AND REDEEM ONLINE AT
• WWW.TOPAZVOUCHERDESK.COM
• Certificate ID # 47261-38504
• Expires 02/29/2020
• *terms and conditions apply see website for details
• KEEP IN MIND THE EXAMPLES I AM UPLOADING ARE SIMPLY TO SHOW YOU THAT THEY CONTAIN THE "COMPLIMENTS OF" AND "EXCLUSIVELY FOR" ELEMENTS. THESE MUST BE INCLUDED IN NEW DESIGN. PLEASE ONLY USE THE CONTENT I PROVIDED IN BRIEF, DONT USE CONTENT FROM EXAMPLES.
Nice to have
• EXCITING LAS VEGAS IMAGES THAT MAKE SOMEONE WANT TO GO THERE

```html
<!DOCTYPE html>
<html lang="en">
<head>
<meta charset="utf-8">
<title>Las Vegas Vacation Gift Certificate</title>
<link rel="stylesheet" href="https://fonts.googleapis.com/css2?family=Lato:ital,wght@0,400;0,700;0,900;1,700&display=swap">
<style>
  :root {
    --page-bg: #6b6b6b;
    --paper: #ffffff;
    --deep-blue: #0b5c91;
    --ocean: #1f6f9a;
    --sage: #9db08c;
    --ribbon-gold: #e9e0a8;
    --ink: #111111;
    --field-bg: #f3f3f3;
    --white: #ffffff;
  }
  * { margin: 0; padding: 0; box-sizing: border-box; }
  html, body { width: 1200px; height: 1200px; overflow: hidden; }
  body { background: var(--page-bg); font-family: "Lato", sans-serif; position: relative; }

  .flyer {
    position: absolute; left: 150px; top: 21px;
    width: 900px; height: 1157px;
    background: var(--paper); overflow: hidden;
  }
  .hero-bg { position: absolute; left: 0; top: 0; width: 900px; height: 800px; }

  .headline {
    position: absolute; left: 0; top: 28px; width: 900px;
    text-align: center; color: var(--white);
    font-style: italic; font-weight: 700; font-size: 26px; line-height: 31px;
    letter-spacing: -0.4px;
  }
  .headline-rule {
    position: absolute; left: 402px; top: 132px; width: 97px; height: 4px;
    background: var(--white);
  }
  .intro {
    position: absolute; left: 40px; top: 155px; width: 820px;
    text-align: center; color: var(--white);
    font-size: 17.5px; line-height: 20.5px; letter-spacing: -0.3px;
  }

  .ribbon {
    position: absolute; background: var(--ribbon-gold); color: var(--ink);
    font-weight: 700; text-align: center;
    clip-path: polygon(0 0, 100% 0, calc(100% - 16px) 50%, 100% 100%, 0 100%, 16px 50%);
  }
  .ribbon-features { left: 342px; top: 247px; width: 227px; height: 42px; font-size: 26px; line-height: 44px; }
  .ribbon-how { left: 228px; top: 428px; width: 420px; height: 42px; font-size: 26px; line-height: 44px; }

  .feature-list { position: absolute; top: 312px; list-style: none; color: var(--white); font-size: 15px; line-height: 25.7px; letter-spacing: -0.3px; }
  .feature-list li { position: relative; padding-left: 16px; }
  .feature-list li::before, .how-list li::before {
    content: ""; position: absolute; left: 0; width: 8px; height: 8px; border-radius: 50%; background: var(--white);
  }
  .feature-list li::before { top: 9px; }
  .col-1 { left: 29px; width: 290px; }
  .col-2 { left: 323px; width: 280px; }
  .col-3 { left: 607px; width: 275px; }

  .how-list { position: absolute; left: 29px; top: 496px; width: 845px; list-style: none; color: var(--white); font-size: 14.6px; line-height: 17.2px; letter-spacing: -0.4px; }
  .how-list li { position: relative; padding-left: 16px; margin-bottom: 8.5px; }
  .how-list li::before { top: 4px; }

  .photo-badge { position: absolute; width: 200px; height: 200px; }
  .badge-left { left: 130px; top: 642px; }
  .badge-mid { left: 345px; top: 668px; }
  .badge-right { left: 563px; top: 642px; }
  .badge-label { font-family: "Lato", sans-serif; font-weight: 700; font-size: 13px; fill: var(--white); }

  .field-title {
    position: absolute; top: 882px; width: 416px; text-align: center;
    color: var(--deep-blue); font-weight: 900; font-size: 22px; letter-spacing: 0.2px;
  }
  .field-title.compliments { left: 34px; }
  .field-title.exclusive { left: 462px; }
  .edit-field {
    position: absolute; top: 917px; width: 416px; height: 133px;
    background: var(--field-bg); border-radius: 10px;
  }
  .edit-field.compliments { left: 34px; }
  .edit-field.exclusive { left: 462px; }

  .certificate-id { position: absolute; left: 32px; top: 1068px; font-weight: 700; font-size: 17.5px; color: var(--ink); }
  .terms { position: absolute; left: 337px; top: 1073px; width: 300px; text-align: center; font-size: 11.5px; color: var(--ink); }
  .expires { position: absolute; right: 35px; top: 1068px; font-weight: 700; font-size: 17.5px; color: var(--ink); }

  .redeem-band {
    position: absolute; left: 0; top: 1100px; width: 900px; height: 57px;
    background: linear-gradient(90deg, var(--ribbon-gold) 0%, var(--deep-blue) 22%, var(--deep-blue) 78%, var(--ribbon-gold) 100%);
    color: var(--white); text-align: center; font-weight: 700; font-size: 15px; line-height: 57px; letter-spacing: 0.1px;
  }
</style>
</head>
<body>
  <div class="flyer">
    <svg class="hero-bg" viewBox="0 0 900 800" aria-hidden="true">
      <defs>
        <linearGradient id="heroGradient" x1="0" y1="1" x2="0.75" y2="0">
          <stop offset="0" stop-color="#b3bf9a"/>
          <stop offset="0.3" stop-color="#6f9c98"/>
          <stop offset="0.6" stop-color="#2a7399"/>
          <stop offset="1" stop-color="#085a90"/>
        </linearGradient>
      </defs>
      <path d="M0 0 H900 V644 Q450 920 0 644 Z" fill="url(#heroGradient)"/>
    </svg>

    <h1 class="headline">There is no doubt that Las Vegas<br>is one of the hottest travel destinations around the world. In fact, some<br>people would even go as far as</h1>
    <div class="headline-rule"></div>
    <p class="intro">saying that perhaps it is THE hottest place to visit. Enjoy up to 4 nights of resort/casino accommodations in exciting Las Vegas, NV. Millions of people travel to this exciting city each year to enjoy its thrills. Thanks to the business you received this certificate from, now you can enjoy exciting Las Vegas, NV too!</p>

    <div class="ribbon ribbon-features">FEATURES:</div>
    <ul class="feature-list col-1">
      <li>Travel 7 Days A Week</li>
      <li>Stay Your Choice Of Nights (1-4 Nights)</li>
      <li>Good For Two Adults &amp; Two Children</li>
    </ul>
    <ul class="feature-list col-2">
      <li>Pay Just The Taxes &amp; Fees</li>
      <li>Multiple Travel Date Requests Allowed</li>
      <li>Fully Transferable To Another Person</li>
    </ul>
    <ul class="feature-list col-3">
      <li>Just A 30 Days Advance Notice Required</li>
      <li>You Will Have 12 Months To Complete Travel After Redemption</li>
    </ul>

    <div class="ribbon ribbon-how">HOW CAN WE DO THIS?</div>
    <ul class="how-list">
      <li>We contract with the world leading hotel chains and resorts to help them fill their otherwise empty rooms.</li>
      <li>We help fill empty rooms which the hotels, resorts and cruise lines turn into additional revenue from other areas of their property and future bookings.</li>
      <li>Hotels rarely experience full occupancy, yet they remain open, providing rooms and services at fixed costs. So when hotels give out their rooms by partnering with marketing companies like us, they might miss out on the room fee, but they already didn't have that in the first place, at least now they have the opportunity to gain a customer for their in-house restaurants, room service, their casinos, an extra day stay, future bookings, etc.</li>
    </ul>

    <svg class="photo-badge badge-left" viewBox="0 0 200 200">
      <defs>
        <linearGradient id="photoNight" x1="0" y1="0" x2="0" y2="1">
          <stop offset="0" stop-color="#141a4a"/><stop offset="0.6" stop-color="#3a3f9a"/><stop offset="1" stop-color="#b5408c"/>
        </linearGradient>
      </defs>
      <circle cx="100" cy="100" r="95" fill="var(--deep-blue)"/>
      <circle cx="100" cy="100" r="89" fill="var(--white)"/>
      <circle cx="100" cy="100" r="85" fill="url(#photoNight)" role="img" aria-label="Photo of the lit-up Las Vegas Boulevard at night"/>
      <polygon points="8,155 192,155 180,186 20,186" fill="var(--deep-blue)"/>
      <text class="badge-label" x="100" y="175" text-anchor="middle">Boulevard in Clark County</text>
    </svg>

    <svg class="photo-badge badge-mid" viewBox="0 0 200 200">
      <defs>
        <linearGradient id="photoSign" x1="0" y1="0" x2="0" y2="1">
          <stop offset="0" stop-color="#2f6fc0"/><stop offset="0.7" stop-color="#6fa3d6"/><stop offset="1" stop-color="#d8b07c"/>
        </linearGradient>
      </defs>
      <circle cx="100" cy="100" r="95" fill="var(--deep-blue)"/>
      <circle cx="100" cy="100" r="89" fill="var(--white)"/>
      <circle cx="100" cy="100" r="85" fill="url(#photoSign)" role="img" aria-label="Photo of the Las Vegas welcome sign with palm trees"/>
      <polygon points="8,158 192,158 180,189 20,189" fill="var(--deep-blue)"/>
      <text class="badge-label" x="100" y="178" text-anchor="middle">las vegas nevada</text>
    </svg>

    <svg class="photo-badge badge-right" viewBox="0 0 200 200">
      <defs>
        <linearGradient id="photoSkyline" x1="0" y1="0" x2="0" y2="1">
          <stop offset="0" stop-color="#cfb2c2"/><stop offset="0.5" stop-color="#9a8a95"/><stop offset="1" stop-color="#7d7566"/>
        </linearGradient>
      </defs>
      <circle cx="100" cy="100" r="95" fill="var(--deep-blue)"/>
      <circle cx="100" cy="100" r="89" fill="var(--white)"/>
      <circle cx="100" cy="100" r="85" fill="url(#photoSkyline)" role="img" aria-label="Photo of the downtown Las Vegas skyline with mountains"/>
      <polygon points="8,155 192,155 180,186 20,186" fill="var(--deep-blue)"/>
      <text class="badge-label" x="100" y="175" text-anchor="middle">downtown skyline</text>
    </svg>

    <h2 class="field-title compliments">COMPLIMENTS OF</h2>
    <h2 class="field-title exclusive">EXCLUSIVELY FOR</h2>
    <div class="edit-field compliments"></div>
    <div class="edit-field exclusive"></div>

    <p class="certificate-id">Certificate ID # 47261-38504</p>
    <p class="terms">*terms and conditions apply see website for details</p>
    <p class="expires">Expires 02/29/2020</p>

    <div class="redeem-band">VIEW ALL THE DETAILS OF THIS SPECIAL OFFER AND REDEEM ONLINE AT&nbsp; WWW.TOPAZVOUCHERDESK.COM</div>
  </div>
</body>
</html>
```